W.I.Q 'Wadi Ibn Qutub' for General Transportation

this company is a Iraqi based company.
It provides a number of logistics activities such as;
Overland Transportation
High and heavy logistics
Customs clearance
warehousing
Automotive logistics
The company has been registered since 2009.
If you have any other questions please feel free to ask.
Target Market(s)
Automotive
White goods
All Trading sectors
Industry/Entity Type
Automotive

```html
<!DOCTYPE html>
<html lang="en">
<head>
<meta charset="utf-8">
<title>Wadi Ibn Qutub Logistics</title>
<link href="https://fonts.googleapis.com/css2?family=Open+Sans:wght@300;400;600;700&display=swap" rel="stylesheet">
<style>
:root{
  --ink:#2b2d38;
  --band:#32343f;
  --accent:#00a8f0;
  --nav-sep:#e8a33b;
  --brand:#123a7a;
  --muted:#8a8d94;
  --faint:#c7cad0;
  --link:#2a8fd8;
  --white:#ffffff;
}
*{box-sizing:border-box;margin:0;padding:0}
html,body{width:1099px;height:1200px;overflow:hidden;background:var(--white);font-family:"Open Sans",Arial,sans-serif;color:var(--ink)}
.page{position:relative;width:1099px;height:1200px}

.site-header{position:absolute;left:0;top:0;width:100%;height:88px;background:var(--white)}
.brand{position:absolute;left:111px;top:20px;width:150px;text-align:center}
.brand-name{display:block;font-size:34px;font-weight:700;letter-spacing:6px;color:var(--brand);line-height:36px}
.brand-sub{display:block;font-size:8px;color:var(--brand);letter-spacing:.5px;line-height:10px}
.main-nav{position:absolute;left:455px;top:33px;display:flex;align-items:center;font-size:10px;letter-spacing:.2px}
.main-nav a{color:var(--ink);text-decoration:none}
.main-nav .sep{display:inline-block;width:1px;height:12px;background:var(--nav-sep);margin:0 20px}
.search{position:absolute;left:866px;top:79px;top:79px}
.search-box{position:absolute;left:866px;top:29px;width:122px;height:24px;background:#f1f1f2;font-size:10px;color:#9a9ca2;padding:6px 7px}
.search-box svg{position:absolute;right:5px;top:4px}

.hero{position:absolute;left:0;top:88px;width:100%;height:443px;background:var(--band)}
.hero-title{position:absolute;left:211px;top:52px;font-size:35px;font-weight:400;color:var(--white);letter-spacing:.2px}
.hero-cta{position:absolute;left:692px;top:53px;width:165px;height:48px;background:var(--accent);color:var(--white);font-size:15px;display:flex;align-items:center;justify-content:center;text-decoration:none}
.slide{position:absolute;left:294px;top:154px;width:514px;height:279px;background:linear-gradient(180deg,#d9dbdc 0%,#9aa0a3 55%,#3f4446 100%)}
.slide-title{position:absolute;left:52px;top:2px;font-size:34px;font-weight:700;letter-spacing:1px;color:#101010}
.slide-sub{position:absolute;left:53px;top:46px;font-size:16px;font-weight:600;color:#4d5154}
.slide-arrow{position:absolute;top:205px}

.services{position:absolute;left:0;top:604px;width:100%}
.service{position:absolute;width:280px;text-align:center}
.service h2{font-size:18px;font-weight:400;letter-spacing:-.3px;color:var(--ink)}
.service-icon{display:block;width:90px;height:92px;margin:4px auto 0}
.service p{margin-top:17px;font-size:9.5px;line-height:18px;color:var(--muted)}
.service .more{display:inline-block;margin-top:10px;font-size:10px;color:var(--link);text-decoration:none}

.clients{position:absolute;left:0;top:890px;width:100%}
.clients h2{position:absolute;left:111px;top:0;font-size:24px;font-weight:400;color:var(--ink)}
.client{position:absolute;top:55px;font-size:26px;font-weight:700;color:var(--faint);letter-spacing:-.5px}

.site-footer{position:absolute;left:0;top:1031px;width:100%;height:169px;background:var(--band);color:var(--white)}
.foot-nav{position:absolute;left:121px;top:46px;display:flex;align-items:center;font-size:10px}
.foot-nav a{color:var(--white);text-decoration:none}
.foot-nav .sep{display:inline-block;width:1px;height:12px;background:var(--nav-sep);margin:0 17px}
.copyright{position:absolute;left:111px;top:75px;font-size:10px}
.copyright span{color:var(--accent)}
.social{position:absolute;left:781px;top:46px;display:flex;gap:10px}
.social span{display:block;width:26px;height:26px;background:#5b5e69}
</style>
</head>
<body>
<div class="page">

  <header class="site-header">
    <div class="brand"><span class="brand-name">W.I.Q</span><span class="brand-sub">Wadi Ibn Qutub Transportation</span></div>
    <nav class="main-nav">
      <a href="#">ABOUT</a><span class="sep"></span>
      <a href="#">SERVICES</a><span class="sep"></span>
      <a href="#">CLIENTS</a><span class="sep"></span>
      <a href="#">CONTACT US</a>
    </nav>
    <div class="search-box">Search
      <svg width="16" height="16" viewBox="0 0 16 16"><circle cx="6.5" cy="6.5" r="5" fill="none" stroke="#a8aaaf" stroke-width="1.6"/><line x1="10" y1="10" x2="15" y2="15" stroke="#a8aaaf" stroke-width="1.8"/></svg>
    </div>
  </header>

  <section class="hero">
    <h1 class="hero-title">We are a Logistics Company</h1>
    <a class="hero-cta" href="#">Learn More</a>
    <svg class="slide-arrow" style="left:114px" width="22" height="40" viewBox="0 0 22 40"><polyline points="19,3 3,20 19,37" fill="none" stroke="#8b8e97" stroke-width="3"/></svg>
    <div class="slide" role="img" aria-label="Photo of a white truck driving on a highway">
      <div class="slide-title">KNOWLEDGEABLE</div>
      <div class="slide-sub">We know everything about Logistics</div>
    </div>
    <svg class="slide-arrow" style="left:966px" width="22" height="40" viewBox="0 0 22 40"><polyline points="3,3 19,20 3,37" fill="none" stroke="#8b8e97" stroke-width="3"/></svg>
  </section>

  <section class="services">
    <div class="service" style="left:99px">
      <h2>OVERLAND TRANSPORTATION</h2>
      <div class="service-icon" role="img" aria-label="Illustration of a delivery truck" style="background:linear-gradient(135deg,#c9d2de,#6f86a8)"></div>
      <p>We provide the right item in the right quantity at the right time at the right place for the right price in the right condition to the right customer.</p>
      <a class="more" href="#">READ MORE</a>
    </div>
    <div class="service" style="left:406px">
      <h2>CUSTOM CLEARANCE</h2>
      <div class="service-icon" role="img" aria-label="Pictogram of a customs officer at a desk" style="background:#1a1a1a"></div>
      <p>We help you to get permission to pass and get national customs authority grants for imported goods so that they can enter the country.</p>
      <a class="more" href="#">READ MORE</a>
    </div>
    <div class="service" style="left:713px">
      <h2>WAREHOUSING</h2>
      <div class="service-icon" role="img" aria-label="Illustration of a forklift carrying boxes" style="background:linear-gradient(135deg,#e6b93a,#d9532a)"></div>
      <p>Configuring and managing warehouses is a central concern for W.I.Q.</p>
      <a class="more" href="#">READ MORE</a>
    </div>
  </section>

  <section class="clients">
    <h2>Clients</h2>
    <svg style="position:absolute;left:118px;top:112px" width="16" height="30" viewBox="0 0 16 30"><polyline points="14,2 2,15 14,28" fill="none" stroke="#c7cad0" stroke-width="3"/></svg>
    <span class="client" style="left:243px">KESTO</span>
    <span class="client" style="left:416px">Flatline Homes</span>
    <span class="client" style="left:616px">NEWSGRID</span>
    <span class="client" style="left:780px">ORVALO</span>
    <svg style="position:absolute;left:972px;top:112px" width="16" height="30" viewBox="0 0 16 30"><polyline points="2,2 14,15 2,28" fill="none" stroke="#c7cad0" stroke-width="3"/></svg>
  </section>

  <footer class="site-footer">
    <nav class="foot-nav">
      <a href="#">Home</a><span class="sep"></span>
      <a href="#">About</a><span class="sep"></span>
      <a href="#">Services</a><span class="sep"></span>
      <a href="#">Clients</a><span class="sep"></span>
      <a href="#">Contact</a>
    </nav>
    <div class="copyright">© 2014 Designed by <span>Loft Pixel</span></div>
    <div class="social" aria-label="Social links">
      <span></span><span></span><span></span><span></span><span></span><span></span>
    </div>
  </footer>

</div>
</body>
</html>
```